Volunteer Marketplace Needs New Look - www.Mipsko.org

Mipsko is the first online marketplace that lets you buy or sell volunteered services to raise money for charity. (www.Mipsko.org)

We went into live testing a few months ago to get some feedback and feel we need to redo the design. Some points:

- The current design was developed when a previous logo was being used. We later developed the current logo (which we love) and have never felt it really fit into the design. A design that plays up the logo would be great but not required.

- The circles in the logo represent coins which is a theme we are using in our branding (our business cards are coins). The marketplace offers a new form of currency people can use to give back. We don't feel the design should center around this concept, but a small element would be a nice touch.

We want a design that is engaging and fun - but still professional and credible.
Updates

I just want to thank you all for submitting designs. I have been trying to send feedback to everyone and am starting to eliminate designs so I can begin to narrow it. It is so hard to decide. You all did a great job! 

Target Market(s)

There are three target audiences - volunteers donating their services, customers buying donated services, and charities joining the program.

Industry/Entity Type

Business

Requirements
Must have
• - We feel we need to represent on the home page the concept of there being two parties that are coming together - the Volunteer and the Customer.

- We have a 60 second overview video in the works that we would like displayed on the home page.
Nice to have
• Incase it is helpful, here are some designs we like - but please know we are looking for creative ideas. Your design does not have to look like these.

http://www.lendora-sample.org/
https://www.wexaro.com/
http://www.layoutbarn.com/website-templates/40056.html
http://www.layoutbarn.com/website-templates/40121.html
http://www.pixelhive.com/

Also - please be creative about what content we put on our home page. We want to modernize the site. We can feed in our blog, twitter, facebook, etc into the home page if you think we should. We need your expertise to recommend what we need to showcase.
Should not have
• Please note that the paragraphs of content do not have to be on the home page. These are there now, but feedback tells us it is too boring - and they is why we are having the video done. So - you do not have to make room for all that text.

```html
<!DOCTYPE html>
<html lang="en">
<head>
<meta charset="utf-8">
<title>Mipsko – The new way to give</title>
<link rel="stylesheet" href="https://fonts.googleapis.com/css2?family=Arimo:wght@400;700&family=Bebas+Neue&family=Questrial&family=Shadows+Into+Light+Two&display=swap">
<style>
  :root{
    --ocean:#3f89a8;
    --ocean-dark:#2f6f8c;
    --lime:#c6dd5f;
    --lime-dark:#a9c93c;
    --teal:#17a393;
    --slate:#4b5a66;
    --ink:#2f3a42;
    --grey:#8a9298;
    --orange:#f0661e;
    --red:#e0201f;
    --white:#ffffff;
    --link:#3a7fa4;
  }
  *{box-sizing:border-box;margin:0;padding:0}
  html,body{width:1200px;height:1120px;overflow:hidden;background:var(--white)}
  body{position:relative;font-family:"Arimo",Arial,sans-serif;color:var(--ink)}
  .abs{position:absolute}

  .top-fade{left:0;top:0;width:1200px;height:40px;background:linear-gradient(#eef0ee,#fff)}

  /* brand */
  .brand{left:216px;top:22px;width:216px}
  .brand-name{display:flex;align-items:center;gap:8px;font-family:"Questrial",sans-serif;font-size:50px;line-height:1;color:var(--slate);letter-spacing:1px}
  .brand-dot{width:18px;height:18px;border-radius:50%;background:var(--ocean)}
  .brand-tag{margin-top:8px;margin-left:64px;font-family:"Arimo",sans-serif;font-size:14px;color:var(--slate)}

  /* search */
  .search{left:553px;top:14px;width:133px;height:17px;border-radius:9px;background:var(--ocean);color:var(--white);font-size:9.5px;line-height:17px;padding-left:11px}

  .account{left:836px;top:-110px;width:148px;height:148px;border-radius:50%;background:radial-gradient(circle at 50% 30%,#3b7f9e,#1f5a72)}
  .account-links{left:868px;top:8px;font-size:8.5px;font-weight:700;color:var(--lime);letter-spacing:.3px;display:flex;gap:14px}

  /* nav */
  .nav-band{left:494px;top:103px;width:489px;height:17px;border-radius:9px;background:var(--lime)}
  .nav-pill{top:102px;height:20px;border-radius:10px;font-size:11px;line-height:20px;text-align:center;color:var(--white)}
  .nav-pill.donated{left:507px;width:151px;background:var(--lime-dark);color:#20343e}
  .nav-pill.wanted{left:690px;width:151px;background:var(--ocean)}
  .nav-pill.how{left:878px;width:86px;background:var(--slate)}

  /* party circles */
  .party{width:220px;height:232px}
  .party.volunteer{left:360px;top:166px}
  .party.customer{left:608px;top:166px}
  .party-title{position:absolute;left:0;width:208px;text-align:center;font-family:"Bebas Neue",sans-serif;font-size:20px;line-height:23px;letter-spacing:.2px}
  .party-text{position:absolute;left:35px;width:140px;font-size:10.5px;font-weight:700;line-height:13.6px}
  .party-cta{position:absolute;left:0;width:208px;text-align:center;font-family:"Bebas Neue",sans-serif;font-size:17px;top:176px}
  .volunteer .party-title{top:46px;color:var(--white)}
  .volunteer .party-text{top:86px;color:var(--lime)}
  .volunteer .party-cta{color:#4a5a3a}
  .customer .party-title{top:33px;color:var(--slate)}
  .customer .party-text{top:93px;color:var(--ocean-dark)}
  .customer .party-cta{color:var(--white)}

  .script{font-family:"Shadows Into Light Two",cursive;color:var(--ocean-dark)}
  .giving{left:868px;top:318px;font-size:18px;line-height:23px;letter-spacing:.5px}
  .giving .watch{color:var(--orange)}

  /* concept */
  .concept-title{left:216px;top:428px;font-family:"Questrial",sans-serif;font-size:23px;letter-spacing:2.5px;color:var(--slate)}
  .concept-copy{left:216px;top:482px;width:466px;font-size:10.6px;line-height:13.6px;color:#333}
  .concept-copy p{margin-bottom:13.2px}
  .cta-line{left:216px;top:780px;font-family:"Bebas Neue",sans-serif;font-size:19px;color:var(--slate)}
  .cta-line .free{color:var(--red)}

  /* video */
  .video{left:734px;top:433px;width:250px;height:171px;border:1px solid #cfd3d5;background:#f4f4f4}
  .video-frame{position:absolute;left:2px;top:3px;width:245px;height:143px;background:linear-gradient(120deg,#4a8a96 0%,#7eb58e 45%,#6cc38a 70%,#c6de62 100%)}
  .video-bar{position:absolute;left:0;bottom:0;width:248px;height:20px;background:linear-gradient(#f2f2f2,#d9d9d9);border-top:1px solid #bbb;font-size:8px;color:#333}

  .help{left:808px;top:764px;font-size:18px;letter-spacing:.5px}
  .charity{left:809px;top:795px;width:174px;height:91px;border:1px solid #9aa0a4;display:flex;align-items:center;justify-content:center;gap:8px}
  .charity-dot{width:30px;height:30px;border-radius:50%;background:var(--red)}
  .charity-name{font-family:"Arimo",sans-serif;font-weight:700;font-size:17px;line-height:18px;color:#1a1a1a}

  /* footer */
  .footer-nav{left:261px;top:956px;display:flex;gap:19px;font-size:9.6px;font-weight:700;color:var(--link)}
  .copyright{left:262px;top:984px;font-size:7.4px;color:var(--grey)}
  .footer-brand{left:261px;top:1008px}
  .footer-brand .brand-name{font-size:28px}
  .footer-brand .brand-dot{width:10px;height:10px}
  .footer-brand .brand-tag{font-size:7.5px;margin:3px 0 0 30px}
  .join{left:842px;top:1004px;font-size:17px}
  .social{width:50px;height:50px;border-radius:50%}
  .social.feed{left:787px;top:1021px;background:radial-gradient(circle at 40% 35%,#d4e56a,#97b52a)}
  .social.bird{left:840px;top:1031px;background:radial-gradient(circle at 40% 35%,#7fd3f0,#2b97c8)}
  .social.book{left:896px;top:1047px;background:radial-gradient(circle at 40% 35%,#7c98cc,#3b5898)}
  .footer-dome{left:0;top:1050px}
  .dome-links{left:295px;top:1098px;display:flex;gap:19px;font-size:9.5px;color:#3d4a1e}
</style>
</head>
<body>
  <div class="abs top-fade"></div>

  <div class="abs brand">
    <div class="brand-name"><span class="brand-dot"></span>Mipsko</div>
    <div class="brand-tag">The new way to give.</div>
  </div>

  <div class="abs search">search donated talent</div>
  <svg class="abs" style="left:690px;top:12px" width="22" height="26" viewBox="0 0 22 26" aria-hidden="true">
    <circle cx="9" cy="9" r="7" fill="#e2ecb0" stroke="#b7cf4a" stroke-width="3"/>
    <line x1="14" y1="15" x2="19" y2="23" stroke="#b7cf4a" stroke-width="4" stroke-linecap="round"/>
  </svg>

  <div class="abs account"></div>
  <div class="abs account-links"><span>LOG IN</span><span>REGISTER</span></div>

  <div class="abs nav-band"></div>
  <div class="abs nav-pill donated">Search Donated services</div>
  <div class="abs nav-pill wanted">Search Help Wanted Ads</div>
  <div class="abs nav-pill how">How it works</div>

  <div class="abs party volunteer">
    <svg width="220" height="232" viewBox="0 0 220 232" aria-hidden="true">
      <ellipse cx="106" cy="212" rx="94" ry="7" fill="#d6ecec" opacity=".8"/>
      <circle cx="104" cy="106" r="104" fill="var(--ocean)"/>
      <path d="M38 172 Q104 110 170 172 Q104 230 38 172Z" fill="var(--lime)"/>
    </svg>
    <div class="party-title">I want to list my talent</div>
    <div class="party-text">Have a talent you would like to donate to help raise money for those in need ?</div>
    <div class="party-cta">Create profile</div>
  </div>

  <div class="abs party customer">
    <svg width="220" height="232" viewBox="0 0 220 232" aria-hidden="true">
      <ellipse cx="106" cy="212" rx="94" ry="7" fill="#d6ecec" opacity=".8"/>
      <circle cx="110" cy="107" r="104" fill="var(--lime)"/>
      <path d="M44 172 Q110 110 176 172 Q110 230 44 172Z" fill="var(--teal)"/>
    </svg>
    <div class="party-title">I want to hire<br>donated talent</div>
    <div class="party-text">Looking for an artist, need a music lesson, searching for a handy man ?</div>
    <div class="party-cta">Create profile</div>
  </div>

  <div class="abs script giving">Giving just<br>got easier<br>with Mipsko !<br><span class="watch">watch video</span></div>
  <svg class="abs" style="left:955px;top:396px" width="32" height="30" viewBox="0 0 32 30" aria-hidden="true">
    <path d="M2 6 Q20 0 18 25 M12 19 L18 26 L26 16" fill="none" stroke="#2f6f8c" stroke-width="1.4"/>
  </svg>

  <h1 class="abs concept-title">THE CONCEPT...</h1>
  <div class="abs concept-copy">
    <p><b>JUST LAUNCHED!</b> Mipsko is hot off the press! Welcome to our first visitors.</p>
    <p>Most people want to make a difference, but getting involved with the cause you care about can be a challenge. That's how Mipsko changes the world of giving!</p>
    <p>Everyone has talents - some professional and some hobbies. Lots of people and companies need people with talent. Mipsko enables those with talent to volunteer their time to those who need to hire people with skills -- while benefiting the charity of your choice.</p>
    <p>Whether you are a landscaper, hairdresser, mechanic, musician, computer programmer, and much more -- if you or your business can perform services people will pay for -- you can volunteer your services for hire and have the payment go to charity.</p>
    <p>Not only can you volunteer your time but by hiring volunteered talent such as babysitters, house cleaners, and more you are spending as you normally would but now you are using your money to change the world!</p>
    <p>Mipsko provides a revolutionary way to volunteer. It's a new currency. It takes valuable volunteer skills and turns them into real money for charities. Everyone has a talent. People spend money to hire people with talent. Charities need money. And now Mipsko brings them all together.</p>
  </div>
  <div class="abs cta-line">Get started by creating a <span class="free">free</span> account!</div>

  <div class="abs video">
    <div class="video-frame" role="img" aria-label="Overview video poster with soft green and teal shapes"></div>
    <svg class="abs" style="left:113px;top:62px" width="44" height="50" viewBox="0 0 44 50" aria-hidden="true">
      <path d="M2 2 L42 25 L2 48Z" fill="#111"/>
    </svg>
    <div class="video-bar">
      <svg width="248" height="20" viewBox="0 0 248 20" aria-hidden="true">
        <path d="M9 5 L18 10 L9 15Z" fill="#222"/>
        <line x1="26" y1="2" x2="26" y2="18" stroke="#bbb"/>
        <path d="M30 8 h3 l4 -3 v10 l-4 -3 h-3Z" fill="#333"/>
        <line x1="48" y1="2" x2="48" y2="18" stroke="#bbb"/>
        <text x="53" y="13" font-size="8" fill="#333" font-family="Arimo,sans-serif">0:00 / 0:00</text>
        <rect x="104" y="8" width="112" height="4" rx="2" fill="#c9c9c9" stroke="#aaa" stroke-width=".5"/>
        <circle cx="108" cy="10" r="5" fill="#eee" stroke="#555"/>
        <path d="M230 6 h3 M230 6 v3 M241 6 h-3 M241 6 v3 M230 15 h3 M230 15 v-3 M241 15 h-3 M241 15 v-3" stroke="#333" stroke-width="1.3" fill="none"/>
      </svg>
    </div>
  </div>

  <div class="abs script help">Help any Charity</div>
  <svg class="abs" style="left:948px;top:770px" width="32" height="26" viewBox="0 0 32 26" aria-hidden="true">
    <path d="M2 6 Q22 0 22 20 M15 15 L22 22 L28 13" fill="none" stroke="#2f6f8c" stroke-width="1.4"/>
  </svg>
  <div class="abs charity">
    <span class="charity-dot"></span>
    <span class="charity-name">Brightpath<br>Kids</span>
  </div>

  <nav class="abs footer-nav">
    <span>Home</span><span>Newsroom</span><span>About Mipsko</span><span>Charities</span><span>FAQ</span><span>Contact Mipsko</span><span>Terms &amp; Conditions</span><span>Privacy Policy</span><span>Blog</span><span>Site Map</span>
  </nav>
  <div class="abs copyright">Copyright © 2012 Mipsko, Inc. All rights reserved.Mipsko® is a registered trademark of Mipsko, Inc. Patent Pending.</div>

  <div class="abs footer-brand">
    <div class="brand-name"><span class="brand-dot"></span>Mipsko</div>
    <div class="brand-tag">The new way to give.</div>
  </div>

  <svg class="abs footer-dome" width="1200" height="70" viewBox="0 0 1200 70" aria-hidden="true">
    <defs>
      <linearGradient id="domeFill" x1="0" y1="0" x2="0" y2="1">
        <stop offset="0" stop-color="#d3e674"/>
        <stop offset="1" stop-color="#a9cb3c"/>
      </linearGradient>
    </defs>
    <path d="M212 70 Q598 -20 984 70Z" fill="url(#domeFill)"/>
  </svg>

  <div class="abs script join">Join Us</div>
  <svg class="abs" style="left:900px;top:1010px" width="30" height="26" viewBox="0 0 30 26" aria-hidden="true">
    <path d="M2 6 Q20 0 20 20 M13 15 L20 22 L26 13" fill="none" stroke="#2f6f8c" stroke-width="1.4"/>
  </svg>
  <div class="abs social feed" aria-label="Feed"></div>
  <div class="abs social bird" aria-label="Social network"></div>
  <div class="abs social book" aria-label="Social network"></div>

  <div class="abs dome-links">
    <span>Volunteer Opportunity</span><span>Volunteering Programs</span><span>Local Volunteer Opportunities</span><span>Local Volunteer Work</span><span>Local Volunteering</span>
  </div>
</body>
</html>
```